A Clear Three Step Roadmap For Contractors

We are looking for a one-pager "roadmap" that is similar to the 2nd picture we attached, but much more professional & better... please make it landscape orientation. The logo for this system is attached below, as well.

Our Brand Colors to use:
#f2d582
#303030
#8b8c90

The copy we'd like to use on the flyer:
A Clear Three Step Roadmap that will finally allow you to attract quality customers and win more jobs.

The Keystone Ladder Method is a simple to follow system that was created specifically for Contractors and Blue Collar Business Owners.

When it comes to marketing and growing their business, the majority of Contractors are left confused, frustrated and extremely overwhelmed. Unlike most sales, marketing & training programs that offer a single "piece of the puzzle", we've mapped out each essential step of the puzzle and cut out all of the fluff.

All you have to do is complete each step in the right order and we'll be guiding you along the entire journey!

A ---> B

Blueprint: Get clear on where you're going, define your ideal audience, and finally, master your message.
Step 1: Clarify The Chaos
Step 2: Define Your Customer
Step 3: Master Your Message

Build: Attract quality leads, Build your funnel and Formulate a high-converting follow-up system
Step 4: Develop Lead Generator
Step 5: Construct Your Funnel
Step 6: Formulate the Follow-Up

Breakthrough: Get in front of your ideal customers and rapidly scale your business by driving traffic and becoming the authority in your market
Step 7: Turn-On the Traffic
Step 8: Become the Authority
Step 9: Unlock Your Growth

```html
<!DOCTYPE html>
<html lang="en">
<head>
<meta charset="utf-8">
<title>Keystone Ladder Method</title>
<link rel="stylesheet" href="https://fonts.googleapis.com/css2?family=Oswald:wght@400;500&family=Rajdhani:wght@400;500;700&family=Lato:wght@400;700&display=swap">
<style>
  :root {
    --gold: #f2d582;
    --charcoal: #303030;
    --slate: #8b8c90;
    --ink: #1c1c1c;
    --paper: #ffffff;
    --road: #c9c9c9;
  }
  * { box-sizing: border-box; margin: 0; padding: 0; }
  html, body { width: 1200px; height: 1200px; overflow: hidden; background: var(--paper); }
  .canvas { position: relative; width: 1200px; height: 1200px; }

  .sheet { position: absolute; left: 146px; width: 915px; box-shadow: 0 4px 14px rgba(0,0,0,.28); }
  .sheet--intro { top: 57px; height: 515px; background: var(--charcoal); }
  .sheet--map { top: 635px; height: 515px; background: radial-gradient(ellipse at 55% 45%, #3a3a3a 0%, #2a2a2a 70%, #222 100%); }

  .masthead { position: absolute; left: 0; top: 0; width: 915px; height: 78px; display: flex; }
  .brand { width: 296px; height: 78px; background: var(--paper); display: flex; align-items: center; padding-left: 29px; gap: 12px; }
  .brand__mark { width: 46px; height: 46px; background: var(--gold); flex: none; }
  .brand__name { font-family: "Rajdhani", sans-serif; font-weight: 700; color: var(--charcoal); font-size: 21px; line-height: 1; text-transform: uppercase; letter-spacing: .3px; }
  .tagline { flex: 1; background: var(--gold); display: flex; align-items: center; padding-left: 25px; padding-right: 20px;
    font-family: "Rajdhani", sans-serif; font-weight: 700; font-size: 19px; line-height: 23px; color: var(--charcoal); text-transform: uppercase; letter-spacing: .4px; }

  .intro-body { position: absolute; left: 29px; top: 105px; width: 385px; font-family: "Rajdhani", sans-serif; font-weight: 500; font-size: 14.2px; line-height: 18.4px; color: #ececec; }
  .intro-body p + p { margin-top: 18px; }

  .preview { position: absolute; left: 432px; top: 90px; width: 459px; height: 271px; background: var(--paper); border-radius: 12px; padding: 14px; }
  .preview svg { display: block; width: 431px; height: 242px; }

  .phases { position: absolute; left: 0; top: 371px; width: 915px; height: 144px; background: var(--gold); }
  .phase { position: absolute; top: 0; width: 280px; text-align: center; }
  .phase__tab { position: relative; margin: 9px auto 0; height: 40px; }
  .phase__tab::after { content: ""; position: absolute; left: 8px; top: 4px; right: -7px; bottom: -3px; border: 1.5px solid var(--ink); border-radius: 0 12px 0 12px; z-index: 0; }
  .phase__title { position: relative; z-index: 1; height: 40px; line-height: 40px; background: linear-gradient(90deg, #111 0%, #3a3a3a 100%); color: var(--paper); border-radius: 12px 0 12px 0;
    font-family: "Rajdhani", sans-serif; font-weight: 700; font-size: 27px; letter-spacing: .5px; }
  .phase__text { margin-top: 14px; font-family: "Lato", sans-serif; font-size: 13.8px; line-height: 17.6px; color: var(--charcoal); }
  .phase--blueprint { left: 152px; margin-left: -140px; }
  .phase--blueprint .phase__tab { width: 184px; }
  .phase--build { left: 435px; margin-left: -140px; }
  .phase--build .phase__tab { width: 156px; }
  .phase--breakthrough { left: 741px; margin-left: -140px; width: 290px; }
  .phase--breakthrough .phase__tab { width: 260px; }
  .divider { position: absolute; top: 24px; height: 100px; border-left: 2px dotted var(--charcoal); }
  .divider--a { left: 299px; }
  .divider--b { left: 571px; }

  .sheet--map svg { display: block; width: 915px; height: 515px; }
  .step-label { font-family: "Oswald", sans-serif; font-weight: 400; font-size: 30px; fill: #f1f1f1; text-anchor: middle; }
  .phase-tag { font-family: "Rajdhani", sans-serif; font-weight: 700; font-size: 32px; fill: var(--charcoal); }
  .phase-num { font-family: "Rajdhani", sans-serif; font-weight: 700; font-size: 36px; fill: var(--charcoal); text-anchor: middle; }
  .endpoint { font-family: "Oswald", sans-serif; font-weight: 500; font-size: 36px; fill: var(--charcoal); text-anchor: middle; }
  .icon { fill: none; stroke: var(--charcoal); stroke-width: 3; stroke-linecap: round; stroke-linejoin: round; }
  .icon-word { font-family: "Rajdhani", sans-serif; font-weight: 700; font-size: 15px; fill: var(--charcoal); text-anchor: middle; }
</style>
</head>
<body>
<div class="canvas">

  <svg width="0" height="0" style="position:absolute">
    <defs>
      <g id="stop">
        <circle r="74" fill="none" stroke="var(--gold)" stroke-width="5" stroke-dasharray="120 112" transform="rotate(-110)"/>
        <circle r="69" fill="var(--charcoal)" stroke="var(--paper)" stroke-width="4"/>
        <circle r="58" fill="var(--gold)"/>
      </g>
      <g id="icon-traffic" class="icon">
        <path d="M0 34 V-26 M-10 -16 L0 -30 L10 -16"/>
        <path d="M0 10 Q0 -4 22 -4 M14 -12 L26 -4 L14 4"/>
        <path d="M0 18 Q0 6 -22 6 M-14 -2 L-26 6 L-14 14"/>
      </g>
      <g id="icon-authority" class="icon">
        <path d="M-32 -8 L0 -26 L32 -8 Z"/>
        <path d="M-22 -2 V22 M-11 -2 V22 M0 -2 V22 M11 -2 V22 M22 -2 V22"/>
        <path d="M-34 24 H34 M-36 31 H36"/>
        <path d="M0 -26 V-40 H13 V-33 H0"/>
      </g>
      <g id="icon-growth" class="icon">
        <path d="M-32 30 H32"/>
        <rect x="-28" y="14" width="10" height="16"/>
        <rect x="-14" y="6" width="10" height="24"/>
        <rect x="0" y="-4" width="10" height="34"/>
        <rect x="14" y="-16" width="10" height="46"/>
        <path d="M-26 2 Q6 -2 26 -30 M16 -30 H26 V-20"/>
        <path d="M-28 -28 H-16 M-28 -22 H-18 M-28 -16 H-16"/>
      </g>
      <g id="icon-follow" class="icon">
        <path d="M-34 -14 H20 L32 0 L20 14 H-6 L-16 24 V14 H-34 Z"/>
        <path d="M-28 20 H-22 M-30 26 H-24"/>
        <text class="icon-word" x="-7" y="5" stroke="none">FOLLOW</text>
      </g>
      <g id="icon-funnel" class="icon">
        <path d="M-28 -8 H28 L8 14 V30 L-8 36 V14 Z"/>
        <circle cx="-14" cy="-22" r="4"/>
        <circle cx="0" cy="-26" r="4"/>
        <circle cx="14" cy="-22" r="4"/>
        <path d="M-26 -30 V-20 M26 -30 V-20"/>
      </g>
      <g id="icon-generator" class="icon">
        <rect x="-30" y="-16" width="60" height="40"/>
        <rect x="-24" y="-10" width="24" height="28"/>
        <path d="M-20 -4 H-4 M-20 4 H-4 M-20 12 H-10"/>
        <path d="M16 -10 L8 4 H16 L10 16"/>
        <path d="M-8 -16 V-24 H8 V-16"/>
        <path d="M-24 24 V30 M24 24 V30"/>
      </g>
      <g id="icon-target" class="icon">
        <circle r="22"/>
        <path d="M0 -36 V-8 M0 8 V36 M-36 0 H-8 M8 0 H36"/>
      </g>
      <g id="icon-customer" class="icon">
        <circle cx="0" cy="-14" r="13"/>
        <path d="M-26 32 Q-26 6 0 6 Q26 6 26 32"/>
        <path d="M-5 8 L0 18 L5 8 M0 18 V30"/>
      </g>
      <g id="icon-megaphone" class="icon">
        <path d="M-26 -10 H-12 L22 -28 V28 L-12 10 H-26 Z"/>
        <path d="M-18 10 V28 H-8 V12"/>
        <path d="M22 -6 Q30 0 22 6"/>
      </g>

      <symbol id="roadmap" viewBox="0 0 1464 824">
        <!-- roads -->
        <rect x="391" y="665" width="863" height="24" fill="var(--road)"/>
        <line x1="391" y1="677" x2="1254" y2="677" stroke="var(--charcoal)" stroke-width="2" stroke-dasharray="10 6"/>
        <rect x="546" y="412" width="708" height="24" fill="var(--road)"/>
        <line x1="546" y1="424" x2="1254" y2="424" stroke="var(--charcoal)" stroke-width="2" stroke-dasharray="10 6"/>
        <rect x="546" y="175" width="852" height="24" fill="var(--road)"/>
        <line x1="546" y1="187" x2="1398" y2="187" stroke="var(--charcoal)" stroke-width="2" stroke-dasharray="10 6"/>
        <rect x="534" y="250" width="24" height="52" fill="var(--road)"/>
        <line x1="546" y1="250" x2="546" y2="302" stroke="var(--charcoal)" stroke-width="2" stroke-dasharray="10 6"/>
        <rect x="1242" y="490" width="24" height="58" fill="var(--road)"/>
        <line x1="1254" y1="490" x2="1254" y2="548" stroke="var(--charcoal)" stroke-width="2" stroke-dasharray="10 6"/>

        <!-- endpoints -->
        <circle cx="391" cy="677" r="28" fill="var(--paper)" stroke="var(--gold)" stroke-width="5"/>
        <text class="endpoint" x="391" y="690">A</text>
        <circle cx="1398" cy="187" r="28" fill="var(--paper)" stroke="var(--gold)" stroke-width="5"/>
        <text class="endpoint" x="1398" y="200">B</text>

        <!-- phase tags -->
        <g>
          <rect x="38" y="150" width="6" height="54" fill="var(--paper)"/>
          <polygon points="54,150 371,150 398,177 371,204 54,204" fill="none" stroke="var(--gold)" stroke-width="2"/>
          <polygon points="50,150 336,150 363,177 336,204 50,204" fill="var(--paper)"/>
          <rect x="50" y="150" width="46" height="54" fill="var(--gold)"/>
          <text class="phase-num" x="73" y="190">3</text>
          <text class="phase-tag" x="108" y="189">BREAKTHROUGH</text>
        </g>
        <g>
          <rect x="38" y="386" width="6" height="54" fill="var(--paper)"/>
          <polygon points="54,386 253,386 280,413 253,440 54,440" fill="none" stroke="var(--gold)" stroke-width="2"/>
          <polygon points="50,386 218,386 245,413 218,440 50,440" fill="var(--paper)"/>
          <rect x="50" y="386" width="46" height="54" fill="var(--gold)"/>
          <text class="phase-num" x="73" y="426">2</text>
          <text class="phase-tag" x="108" y="425">BUILD</text>
        </g>
        <g>
          <rect x="38" y="647" width="6" height="54" fill="var(--paper)"/>
          <polygon points="54,647 299,647 326,674 299,701 54,701" fill="none" stroke="var(--gold)" stroke-width="2"/>
          <polygon points="50,647 266,647 293,674 266,701 50,701" fill="var(--paper)"/>
          <rect x="50" y="647" width="46" height="54" fill="var(--gold)"/>
          <text class="phase-num" x="73" y="687">1</text>
          <text class="phase-tag" x="108" y="686">BLUEPRINT</text>
        </g>

        <!-- stops -->
        <use href="#stop" x="546" y="187"/>
        <use href="#stop" x="904" y="187"/>
        <use href="#stop" x="1254" y="187"/>
        <use href="#stop" x="546" y="424"/>
        <use href="#stop" x="904" y="424"/>
        <use href="#stop" x="1254" y="424"/>
        <use href="#stop" x="546" y="677"/>
        <use href="#stop" x="904" y="677"/>
        <use href="#stop" x="1254" y="677"/>

        <!-- icons -->
        <use href="#icon-traffic" x="546" y="187"/>
        <use href="#icon-authority" x="904" y="187"/>
        <use href="#icon-growth" x="1254" y="187"/>
        <use href="#icon-follow" x="546" y="424"/>
        <use href="#icon-funnel" x="904" y="424"/>
        <use href="#icon-generator" x="1254" y="424"/>
        <use href="#icon-target" x="546" y="677"/>
        <use href="#icon-customer" x="904" y="677"/>
        <use href="#icon-megaphone" x="1254" y="677"/>

        <!-- step labels -->
        <text class="step-label" x="546" y="97">Turn-On the Traffic</text>
        <text class="step-label" x="904" y="97">Become the Authority</text>
        <text class="step-label" x="1252" y="97">Unlock Your Growth</text>
        <text class="step-label" x="542" y="337">Formulate the Follow-Up</text>
        <text class="step-label" x="906" y="339">Construct Your Funnel</text>
        <text class="step-label" x="1254" y="337">Develop Lead Generator</text>
        <text class="step-label" x="546" y="579">Clarify The Chaos</text>
        <text class="step-label" x="902" y="581">Define Your Customer</text>
        <text class="step-label" x="1252" y="579">Master Your Message</text>
      </symbol>
    </defs>
  </svg>

  <section class="sheet sheet--intro">
    <header class="masthead">
      <div class="brand">
        <span class="brand__mark"></span>
        <span class="brand__name">Keystone Ladder<br>Method</span>
      </div>
      <div class="tagline">A clear three step roadmap that will finally allow you to attract quality customers and win more jobs.</div>
    </header>

    <div class="intro-body">
      <p>The Keystone Ladder Method is a simple to follow system that was created specifically for Contractors and Blue Collar Business Owners.</p>
      <p>When it comes to marketing and growing their business, the majority of Contractors are left confused, frustrated and extremely overwhelmed. Unlike most sales, marketing &amp; training programs that offer a single "piece of the puzzle", we've mapped out each essential step of the puzzle and cut out all of the fluff.</p>
      <p>All you have to do is complete each step in the right order and we'll be guiding you along the entire journey!</p>
    </div>

    <div class="preview">
      <svg viewBox="0 0 1464 824" aria-hidden="true">
        <rect width="1464" height="824" fill="#2c2c2c"/>
        <use href="#roadmap" width="1464" height="824"/>
      </svg>
    </div>

    <div class="phases">
      <div class="phase phase--blueprint">
        <div class="phase__tab"><div class="phase__title">BLUEPRINT</div></div>
        <p class="phase__text">Get clear on where you're going,<br>define your ideal audience, and finally,<br>master your message.</p>
      </div>
      <div class="divider divider--a"></div>
      <div class="phase phase--build">
        <div class="phase__tab"><div class="phase__title">BUILD</div></div>
        <p class="phase__text">Attract quality leads, Build your<br>funnel and Formulate a<br>high-converting follow-up system</p>
      </div>
      <div class="divider divider--b"></div>
      <div class="phase phase--breakthrough">
        <div class="phase__tab"><div class="phase__title">BREAKTHROUGH</div></div>
        <p class="phase__text">Get in front of your ideal customers and<br>rapidly scale your business by driving traffic<br>and becoming the authority in your market</p>
      </div>
    </div>
  </section>

  <section class="sheet sheet--map">
    <svg viewBox="0 0 1464 824">
      <use href="#roadmap" width="1464" height="824"/>
    </svg>
  </section>

</div>
</body>
</html>
```